Business Card cabinets and cabinets components making company.

the card should be formal and interesting at the same time. The main colors will be black and white.

Font styles to use
Sans Serif

Colors

Designer to choose only greyscale colors for use in the design.

Requirements
Must have
• At least must have the followings:
office phone
cell phone
address
position
name
email
web

```html
<!DOCTYPE html>
<html lang="en">
<head>
<meta charset="UTF-8">
<title>Trimwell Business Card</title>
<link rel="stylesheet" href="https://fonts.googleapis.com/css2?family=Montserrat:wght@400;500;700;800&display=swap">
<style>
  :root {
    --ink: #0f0f0f;
    --paper: #ffffff;
    --stage: #4a4b4d;
    --muted: #9a9a9a;
    --soft: #d8d8d8;
  }
  * { box-sizing: border-box; margin: 0; padding: 0; }
  html, body { width: 1200px; height: 900px; overflow: hidden; }
  body {
    background: var(--stage);
    font-family: "Montserrat", sans-serif;
    position: relative;
  }
  .card {
    position: absolute;
    width: 680px;
    height: 388px;
    overflow: hidden;
  }
  .card-front { left: 260px; top: 40px; background: var(--ink); }
  .card-back { left: 260px; top: 472px; background: var(--paper); }

  /* shared brand lockup */
  .brand {
    position: absolute;
    display: flex;
    flex-direction: column;
    align-items: center;
  }
  .brand-row { display: flex; align-items: center; gap: 12px; }
  .brand-square { width: 22px; height: 22px; }
  .brand-name {
    font-weight: 800;
    font-size: 58px;
    letter-spacing: 1px;
    line-height: 1;
  }
  .brand-rule { height: 3px; width: 300px; margin-top: 10px; }

  /* front */
  .card-front .brand { left: 0; right: 0; top: 130px; }
  .card-front .brand-name { color: var(--paper); }
  .card-front .brand-square { background: var(--paper); }
  .card-front .brand-rule { background: var(--paper); }
  .front-bar-top { position: absolute; left: 30px; top: 12px; width: 560px; height: 11px; background: var(--paper); }
  .front-bar-bottom { position: absolute; left: 260px; bottom: 12px; width: 408px; height: 11px; background: var(--paper); }
  .hatch {
    position: absolute;
    background: repeating-linear-gradient(160deg, var(--paper) 0 4px, transparent 4px 8px);
  }
  .front-hatch-right { right: 14px; top: 34px; width: 24px; height: 120px; }
  .front-hatch-left { left: 12px; top: 220px; width: 26px; height: 140px; }
  .front-web {
    position: absolute; left: 0; right: 0; top: 318px;
    text-align: center; color: var(--soft);
    font-size: 11px; letter-spacing: 0.6px;
  }

  /* back */
  .back-info {
    position: absolute; right: 0; top: 0;
    width: 268px; height: 100%;
    background: var(--ink);
    color: var(--paper);
  }
  .card-back .brand { left: 40px; width: 360px; top: 150px; }
  .card-back .brand-name { color: var(--ink); font-size: 50px; }
  .card-back .brand-square { background: var(--ink); }
  .card-back .brand-rule { background: var(--ink); width: 270px; }
  .back-bar-left { position: absolute; left: 22px; top: 160px; width: 13px; height: 228px; background: var(--ink); }
  .back-bar-upper { position: absolute; left: 384px; top: 0; width: 14px; height: 80px; background: var(--ink); clip-path: polygon(0 0,100% 0,100% 100%,0 85%); }
  .back-bar-lower { position: absolute; left: 384px; top: 290px; width: 14px; height: 98px; background: var(--ink); clip-path: polygon(0 0,100% 12%,100% 100%,0 100%); }
  .back-hatch {
    position: absolute; left: 380px; top: 100px; width: 28px; height: 170px;
    background: repeating-linear-gradient(160deg, var(--ink) 0 1.5px, transparent 1.5px 10px);
  }

  .person { position: absolute; left: 26px; top: 52px; display: flex; gap: 14px; align-items: center; }
  .person-icon { width: 40px; height: 40px; }
  .person-name { font-weight: 700; font-size: 21px; letter-spacing: 0.5px; }
  .person-role { font-size: 12px; color: var(--muted); margin-top: 2px; }

  .contact-list { position: absolute; left: 30px; top: 138px; list-style: none; }
  .contact-item { display: flex; align-items: center; gap: 14px; margin-bottom: 14px; min-height: 32px; }
  .contact-icon {
    width: 30px; height: 30px; border-radius: 6px;
    background: var(--paper); flex: none;
    display: flex; align-items: center; justify-content: center;
  }
  .contact-icon svg { width: 18px; height: 18px; }
  .contact-text { font-size: 11px; line-height: 1.45; color: var(--soft); letter-spacing: 0.3px; }
</style>
</head>
<body>

<section class="card card-front" aria-label="Card front">
  <div class="front-bar-top"></div>
  <div class="hatch front-hatch-right"></div>
  <div class="hatch front-hatch-left"></div>
  <div class="brand">
    <div class="brand-row"><span class="brand-square"></span><span class="brand-name">Trimwell</span></div>
    <div class="brand-rule"></div>
  </div>
  <p class="front-web">www.trimwellcabinets.com</p>
  <div class="front-bar-bottom"></div>
</section>

<section class="card card-back" aria-label="Card back">
  <div class="back-bar-left"></div>
  <div class="brand">
    <div class="brand-row"><span class="brand-square"></span><span class="brand-name">Trimwell</span></div>
    <div class="brand-rule"></div>
  </div>
  <div class="back-bar-upper"></div>
  <div class="back-hatch"></div>
  <div class="back-bar-lower"></div>

  <div class="back-info">
    <div class="person">
      <svg class="person-icon" viewBox="0 0 40 40" aria-hidden="true">
        <circle cx="20" cy="13" r="8" fill="#fff"/>
        <path d="M4 38c0-9 7-15 16-15s16 6 16 15z" fill="#fff"/>
      </svg>
      <div>
        <p class="person-name">DANIEL REEVES</p>
        <p class="person-role">Founder</p>
      </div>
    </div>

    <ul class="contact-list">
      <li class="contact-item">
        <span class="contact-icon">
          <svg viewBox="0 0 24 24" aria-hidden="true"><path d="M6.6 10.8a15 15 0 0 0 6.6 6.6l2.2-2.2c.3-.3.7-.4 1-.2 1.1.4 2.3.6 3.6.6.6 0 1 .4 1 1V20c0 .6-.4 1-1 1A17 17 0 0 1 3 4c0-.6.4-1 1-1h3.5c.6 0 1 .4 1 1 0 1.3.2 2.5.6 3.6.1.3 0 .7-.2 1z" fill="#0f0f0f"/></svg>
        </span>
        <span class="contact-text">Office 555-014-2290<br>Cell 555-014-2291</span>
      </li>
      <li class="contact-item">
        <span class="contact-icon">
          <svg viewBox="0 0 24 24" aria-hidden="true"><rect x="3" y="6" width="18" height="12" fill="none" stroke="#0f0f0f" stroke-width="2"/><path d="M3 6l9 7 9-7" fill="none" stroke="#0f0f0f" stroke-width="2"/></svg>
        </span>
        <span class="contact-text">hello@trimwellcabinets.com</span>
      </li>
      <li class="contact-item">
        <span class="contact-icon">
          <svg viewBox="0 0 24 24" aria-hidden="true"><circle cx="12" cy="12" r="9" fill="none" stroke="#0f0f0f" stroke-width="2"/><ellipse cx="12" cy="12" rx="4" ry="9" fill="none" stroke="#0f0f0f" stroke-width="1.6"/><path d="M3 12h18" stroke="#0f0f0f" stroke-width="1.6"/></svg>
        </span>
        <span class="contact-text">www.trimwellcabinets.com</span>
      </li>
      <li class="contact-item">
        <span class="contact-icon">
          <svg viewBox="0 0 24 24" aria-hidden="true"><path d="M12 2a7 7 0 0 0-7 7c0 5 7 13 7 13s7-8 7-13a7 7 0 0 0-7-7z" fill="#0f0f0f"/><circle cx="12" cy="9" r="2.6" fill="#fff"/></svg>
        </span>
        <span class="contact-text">4810 Birch Hollow Lane<br>Ashford, VA 23000</span>
      </li>
    </ul>
  </div>
</section>

</body>
</html>
```